Golden Era Hollywood Movie Poster Design for a Wedding Invitation

We're looking for a movie poster designed along the lines of the styles of posters in the included "posters" file. We're thinking the "title" of the "movie" should be "The Wedding of the Year". This will be for a wedding invitation to the wedding of "Marla Vostenkiew" and "Daniel Ferroway", so their names should be featured as the "stars" of the movie. The wedding will take place at Cal Brindle Studios in Hollywood, so you can put on the poster "Presented by Cal Brindle Studios". The other uploaded files are photos of the bride and groom. You don't need to use any of the poses in those photos - we'd like to have a pose that's along the lines of the examples in the "posters" file - but I included the photos of the bride and groom as references to help you make the final poster look like them (but in the style of an old Hollywood movie poster). Make them look beautiful and glamorous like stars in a movie from Hollywood's golden era. :)

Project Deadline Extended
Reason: The designs we've received so far aren't quite giving exactly the old-Hollywood feel we're looking for, so we're giving one 5-day extension to see additional designs.

```html
<!DOCTYPE html>
<html lang="en">
<head>
<meta charset="utf-8">
<title>The Wedding of the Year</title>
<link rel="stylesheet" href="https://fonts.googleapis.com/css2?family=Great+Vibes&family=Poiret+One&family=Josefin+Sans:wght@600&display=swap">
<style>
  :root {
    --plum: #8a5a7d;
    --plum-light: #b48aa7;
    --plum-pale: #d9bfd0;
    --plum-deep: #6e4262;
    --ink: #000000;
    --white: #ffffff;
    --name-plum: #8c5a80;
  }
  * { margin: 0; padding: 0; box-sizing: border-box; }
  html, body { width: 928px; height: 1200px; overflow: hidden; background: var(--ink); }
  .poster {
    position: relative;
    width: 928px;
    height: 1200px;
    overflow: hidden;
    background: radial-gradient(ellipse 70% 55% at 30% 35%, var(--plum-light) 0%, var(--plum) 55%, var(--plum-deep) 100%);
  }
  .ground { position: absolute; inset: 0; width: 928px; height: 1200px; }
  .couple-photo {
    position: absolute;
    left: 24px;
    top: 84px;
    width: 420px;
    height: 800px;
    border-radius: 210px 170px 0 0;
    background: linear-gradient(180deg, #8e1f42 0%, #7a2340 18%, #3c2a36 42%, #141014 70%, var(--ink) 100%);
  }
  .title {
    position: absolute;
    inset: 0;
    font-family: "Great Vibes", cursive;
    font-weight: 400;
    color: var(--white);
    line-height: 1;
  }
  .title span { position: absolute; white-space: nowrap; }
  .title .t-the { left: 462px; top: 78px; font-size: 128px; }
  .title .t-wedding { left: 480px; top: 196px; font-size: 106px; }
  .title .t-of { left: 484px; top: 298px; font-size: 64px; }
  .title .t-the2 { left: 522px; top: 350px; font-size: 72px; }
  .title .t-year { left: 614px; top: 312px; font-size: 118px; }
  .billing {
    position: absolute;
    top: 872px;
    left: 0;
    width: 928px;
    height: 136px;
    font-family: "Poiret One", sans-serif;
    color: var(--name-plum);
    -webkit-text-stroke: 1.6px var(--name-plum);
    font-size: 62px;
    line-height: 1;
  }
  .star { position: absolute; top: 0; }
  .star-groom { left: 130px; width: 256px; }
  .star-bride { left: 486px; width: 372px; }
  .name-line { display: flex; justify-content: space-between; height: 66px; align-items: center; }
  .divider {
    position: absolute;
    left: 444px;
    top: 0;
    width: 2px;
    height: 136px;
    background: var(--name-plum);
    opacity: 0.6;
  }
  .presenter {
    position: absolute;
    top: 1052px;
    left: 0;
    width: 928px;
    text-align: center;
    font-family: "Josefin Sans", sans-serif;
    font-weight: 600;
    font-size: 36px;
    line-height: 1;
    letter-spacing: 1px;
    color: var(--white);
    text-transform: uppercase;
    transform: scaleY(1.3);
    transform-origin: center top;
  }
</style>
</head>
<body>
<main class="poster">
  <svg class="ground" viewBox="0 0 928 1200" aria-hidden="true">
    <path d="M0 712 Q 470 560 928 540 L928 620 Q 470 630 0 790 Z" fill="var(--plum-pale)" opacity="0.45"/>
    <path d="M0 752 Q 470 598 928 582 L928 620 Q 470 630 0 790 Z" fill="var(--plum-pale)" opacity="0.6"/>
    <path d="M0 790 Q 470 630 928 620 L928 1200 L0 1200 Z" fill="var(--ink)"/>
  </svg>

  <div class="couple-photo" role="img" aria-label="Portrait of the bride and groom standing together under a red umbrella, holding hands"></div>

  <h1 class="title" aria-label="The Wedding of the Year">
    <span class="t-the">The</span>
    <span class="t-wedding">Wedding</span>
    <span class="t-of">of</span>
    <span class="t-the2">the</span>
    <span class="t-year">Year</span>
  </h1>

  <section class="billing">
    <div class="star star-groom" aria-label="Daniel Ferroway">
      <div class="name-line"><span>D</span><span>A</span><span>N</span><span>I</span><span>E</span><span>L</span></div>
      <div class="name-line"><span>F</span><span>E</span><span>R</span><span>R</span><span>O</span><span>W</span><span>A</span><span>Y</span></div>
    </div>
    <div class="divider"></div>
    <div class="star star-bride" aria-label="Marla Vostenkiew">
      <div class="name-line"><span>M</span><span>A</span><span>R</span><span>L</span><span>A</span></div>
      <div class="name-line"><span>V</span><span>O</span><span>S</span><span>T</span><span>E</span><span>N</span><span>K</span><span>I</span><span>E</span><span>W</span></div>
    </div>
  </section>

  <p class="presenter">Presented by Cal Brindle Studios</p>
</main>
</body>
</html>
```